Dental Co needs single page print ad

Dental company needs a 1 page ad for trade magazines.
I am uploading an example of what we want (words). We need you to make it look great. It can include people or not.
The uploaded ad isn't there to be copied, just to kind of frame what we are thinking. We are open to any design
One page ad
Size 1)

Trim Size - 8 x 10.5
Bleed Size - 8.25 x 10.75
Live Area - 7 x 10

Size 2)

Trim - 8 x 10.875
Bleed - 8.25 x 11.125
Live Area - 7 x 9.875

BRIX Brand Hex #'s

Orange - ff6319
Teal - 56b1bf
Lt. Teal - aed9da
Blue: #38394B

Target Market(s)

Dentists

Requirements
Must have
• BRIX Logo, pic of the sensor (called VANT)
Use the brand hex colors:
Orange - ff6319
Teal - 56b1bf
Lt. Teal - aed9da
Blue: #38394B

```html
<!DOCTYPE html>
<html lang="en">
<head>
<meta charset="utf-8">
<title>VANT Sensor Subscription – Print Ad</title>
<link rel="stylesheet" href="https://fonts.googleapis.com/css2?family=Montserrat:wght@300;400;500;600;700;800&family=Great+Vibes&display=swap">
<style>
  :root {
    --orange: #ff6319;
    --navy: #2d3181;
    --ink: #1e2156;
    --white: #ffffff;
    --stage: #5b5b5b;
    --sensor-dark: #23253f;
    --sensor-light: #6c6e88;
  }
  * { margin: 0; padding: 0; box-sizing: border-box; }
  html, body { width: 1200px; height: 864px; overflow: hidden; }
  body { background: var(--stage); position: relative; font-family: "Montserrat", sans-serif; }
  .ad { position: absolute; display: block; box-shadow: 0 8px 24px rgba(0,0,0,.35); }
  .ad--size1 { left: 86px; top: 106px; width: 467px; height: 609px; }
  .ad--size2 { left: 646px; top: 85px; width: 468px; height: 630px; }
  .size-label {
    position: absolute; top: 770px; width: 400px; text-align: center;
    color: var(--white); font-weight: 700; font-size: 29px; letter-spacing: .5px;
  }
  .size-label--1 { left: 100px; }
  .size-label--2 { left: 656px; }
  .t-kicker { font-family: "Montserrat", sans-serif; font-weight: 300; font-size: 44px; fill: var(--navy); }
  .t-headline { font-family: "Montserrat", sans-serif; font-weight: 600; font-size: 46px; fill: var(--white); letter-spacing: 1px; }
  .t-script { font-family: "Great Vibes", cursive; font-size: 44px; fill: var(--white); }
  .t-stat { font-family: "Montserrat", sans-serif; font-weight: 500; font-size: 22px; fill: var(--white); }
  .t-product { font-family: "Montserrat", sans-serif; font-weight: 800; font-size: 92px; fill: var(--navy); }
  .t-price { font-family: "Montserrat", sans-serif; font-weight: 800; font-size: 52px; fill: var(--orange); }
  .t-terms { font-family: "Montserrat", sans-serif; font-weight: 500; font-size: 31px; fill: var(--white); }
  .t-your { font-family: "Montserrat", sans-serif; font-weight: 700; font-size: 33px; fill: var(--white); }
  .t-decision { font-family: "Montserrat", sans-serif; font-weight: 700; font-size: 33px; fill: var(--orange); }
  .t-benefit { font-family: "Montserrat", sans-serif; font-weight: 400; font-size: 21px; fill: var(--white); }
  .t-phone { font-family: "Montserrat", sans-serif; font-weight: 700; font-size: 42px; fill: var(--white); }
  .t-web { font-family: "Montserrat", sans-serif; font-weight: 500; font-size: 27px; fill: var(--white); letter-spacing: 1.5px; }
  .t-brand { font-family: "Montserrat", sans-serif; font-weight: 800; fill: var(--ink); }
</style>
</head>
<body>

<svg class="ad ad--size1" viewBox="0 0 884 1151" aria-label="Print ad, size 1">
  <defs>
    <linearGradient id="sensorTone" x1="0" y1="0" x2="0.3" y2="1">
      <stop offset="0" stop-color="var(--sensor-dark)"/>
      <stop offset="1" stop-color="var(--sensor-light)"/>
    </linearGradient>

    <g id="headline-block">
      <rect x="61" y="67" width="761" height="58" fill="var(--white)"/>
      <text class="t-kicker" x="441" y="113" text-anchor="middle">A SUBSCRIPTION OPTION FOR</text>
      <text class="t-headline" x="441" y="178" text-anchor="middle">INTRA-ORAL SENSORS IS DUMB.</text>
      <text class="t-script" x="441" y="236" text-anchor="middle">(until you do the math).</text>
    </g>

    <g id="product-block">
      <g role="img" aria-label="Photo of the VANT intra-oral sensor with its cable">
        <rect x="116" y="277" width="412" height="317" rx="70" fill="url(#sensorTone)"/>
      </g>
      <text class="t-stat" x="564" y="332">11 Million X-rays and</text>
      <text class="t-stat" x="564" y="360">Counting</text>
      <text class="t-product" x="570" y="525">VANT</text>
    </g>

    <g id="offer-block">
      <rect x="91" y="650" width="272" height="66" fill="var(--white)"/>
      <rect x="91" y="716" width="272" height="87" fill="var(--orange)"/>
      <text class="t-price" x="227" y="705" text-anchor="middle">$1,999</text>
      <text class="t-terms" x="227" y="753" text-anchor="middle">ONE-TIME</text>
      <text class="t-terms" x="227" y="786" text-anchor="middle">SIGN UP FEE</text>

      <rect x="91" y="827" width="272" height="66" fill="var(--white)"/>
      <rect x="91" y="893" width="272" height="87" fill="var(--orange)"/>
      <text class="t-price" x="227" y="884" text-anchor="middle">$139/mo</text>
      <text class="t-terms" x="227" y="931" text-anchor="middle">CANCEL</text>
      <text class="t-terms" x="227" y="964" text-anchor="middle">ANYTIME</text>

      <text class="t-your" x="411" y="697">YOUR</text>
      <text class="t-decision" x="411" y="736">VANT DECISION</text>
      <line x1="411" y1="757" x2="827" y2="757" stroke="var(--white)" stroke-width="1.2" opacity=".8"/>

      <g class="benefit-ticks" fill="none" stroke="var(--orange)" stroke-width="1.6">
        <circle cx="419" cy="789" r="7"/><path d="M415 789l3 3 5-5"/>
        <circle cx="419" cy="822" r="7"/><path d="M415 822l3 3 5-5"/>
        <circle cx="419" cy="856" r="7"/><path d="M415 856l3 3 5-5"/>
        <circle cx="419" cy="889" r="7"/><path d="M415 889l3 3 5-5"/>
        <circle cx="419" cy="922" r="7"/><path d="M415 922l3 3 5-5"/>
      </g>
      <text class="t-benefit" x="438" y="796">Lifetime $0 deductible warranty</text>
      <text class="t-benefit" x="438" y="829">Unlimited support &amp; upgrades</text>
      <text class="t-benefit" x="438" y="863">Direct integration w/all major software</text>
      <text class="t-benefit" x="438" y="896">Affordable enough for every op</text>
      <text class="t-benefit" x="438" y="929">Preserve your capital</text>
    </g>

    <g id="contact-block">
      <g class="phone-icon" fill="none" stroke="var(--white)" stroke-width="2.5">
        <circle cx="90" cy="1033" r="19"/>
        <path d="M83 1022c-3 2-4 6-2 10 3 7 8 12 14 14 3 1 6 0 8-2l-5-5-3 2c-3-1-6-4-7-7l2-3z" fill="var(--white)" stroke="none"/>
      </g>
      <text class="t-phone" x="122" y="1048">(555) 234-BRIX</text>
      <g class="web-icon" fill="none" stroke="var(--white)" stroke-width="2">
        <circle cx="80" cy="1088" r="10"/>
        <ellipse cx="80" cy="1088" rx="4.5" ry="10"/>
        <line x1="70" y1="1088" x2="90" y2="1088"/>
      </g>
      <text class="t-web" x="98" y="1097">www.BrixImaging.com</text>
      <text class="t-brand" x="712" y="1058" font-size="80" text-anchor="middle">BRIX</text>
      <text class="t-brand" x="712" y="1094" font-size="30" text-anchor="middle" letter-spacing="4">IMAGING</text>
    </g>
  </defs>

  <rect width="884" height="1151" fill="var(--orange)"/>
  <rect x="0" y="461" width="884" height="163" fill="var(--white)"/>
  <rect x="500" y="404" width="384" height="220" fill="var(--white)"/>
  <path d="M0 624H505C540 624 545 574 580 574H884V1151H0Z" fill="var(--navy)"/>
  <path d="M0 1001H545L508 1061H0Z" fill="var(--orange)"/>
  <path d="M884 966H578Q556 966 545 985L470 1118Q462 1133 445 1133H0V1151H884Z" fill="var(--white)"/>

  <use href="#headline-block"/>
  <use href="#product-block"/>
  <use href="#offer-block"/>
  <use href="#contact-block"/>
</svg>

<svg class="ad ad--size2" viewBox="0 0 884 1192" aria-label="Print ad, size 2">
  <rect width="884" height="1192" fill="var(--orange)"/>
  <rect x="0" y="477" width="884" height="170" fill="var(--white)"/>
  <rect x="500" y="418" width="384" height="229" fill="var(--white)"/>
  <path d="M0 647H505C540 647 540 595 575 595H884V1192H0Z" fill="var(--navy)"/>
  <path d="M0 1037H540L503 1100H0Z" fill="var(--orange)"/>
  <path d="M884 1000H575Q553 1000 542 1019L460 1160Q452 1175 435 1175H0V1192H884Z" fill="var(--white)"/>

  <use href="#headline-block" y="11"/>
  <use href="#product-block" y="12"/>
  <use href="#offer-block" y="22"/>
  <use href="#contact-block" y="38"/>
</svg>

<p class="size-label size-label--1">Size 1 - 8.25 x 10.75</p>
<p class="size-label size-label--2">Size 2 - 8.25 x 11.125</p>

</body>
</html>
```